Inspirational speaker and coach Corinne Valdaux is building a website

Design, Create and launch a 10-15 page Wordpress website. Please research Corinne online and use examples you have access to.

```html
<!DOCTYPE html>
<html lang="en">
<head>
<meta charset="utf-8">
<title>Corinne Valdaux — Inspirational Speaker and Coach</title>
<link href="https://fonts.googleapis.com/css2?family=Poppins:wght@400;500;600;700;800&family=Roboto:wght@400;500;700&family=Great+Vibes&display=swap" rel="stylesheet">
<style>
:root{
  --red:#ee1c2e;
  --red-dark:#c9121f;
  --ink:#1e1e1e;
  --charcoal:#2b2b2b;
  --slate:#454545;
  --grey:#7a7a7a;
  --light:#efefef;
  --line:#dcdcdc;
  --white:#ffffff;
}
*{box-sizing:border-box;margin:0;padding:0}
html,body{width:1200px;height:5025px;overflow:hidden}
body{position:relative;background:var(--white);font-family:"Roboto",Arial,sans-serif;color:var(--ink)}
.abs{position:absolute}
.heading{font-family:"Poppins",Arial,sans-serif;font-weight:800;text-transform:uppercase}
.script{font-family:"Great Vibes",cursive}
.btn{position:absolute;display:flex;align-items:center;justify-content:center;gap:8px;font-family:"Poppins",Arial,sans-serif;font-weight:600;font-size:13px;color:var(--white);text-transform:uppercase;border-radius:3px}
.btn-red{background:var(--red)}
.btn-dark{background:var(--charcoal)}

/* header */
.site-header{top:0;left:0;width:1200px;height:86px;background:var(--white);border-bottom:1px solid #eee}
.brand-name{left:102px;top:10px;font-family:"Poppins",sans-serif;font-weight:600;font-size:26px;color:var(--red)}
.brand-tag{left:108px;top:64px;font-size:11px;color:var(--grey);border-top:1px solid var(--red);padding-top:2px}
.nav{left:362px;top:35px;display:flex;gap:26px;font-family:"Poppins",sans-serif;font-weight:600;font-size:13px;text-transform:uppercase;color:var(--ink)}
.nav .active{color:var(--red)}

/* hero */
.hero{top:86px;left:0;width:1200px;height:560px;background:linear-gradient(90deg,#1f1f1f,#3a3a3a)}
.hero-photo{right:0;top:0;width:640px;height:560px;background:radial-gradient(ellipse at 60% 40%,#d9b59c 0%,#a98c78 35%,#5e534c 70%,#3a3a3a 100%)}
.hero-title{left:108px;top:118px;font-size:72px;line-height:74px;color:var(--white)}
.hero-title .accent{color:var(--red)}
.hero-sub{left:110px;top:376px;font-family:"Poppins",sans-serif;font-weight:600;font-size:15px;color:var(--white)}
.hero-sign{left:368px;top:424px;width:184px;height:66px;background:linear-gradient(90deg,rgba(212,175,55,.25),rgba(212,175,55,.45));border-radius:30px}

/* trusted */
.trusted-title{top:728px;width:1200px;text-align:center;font-size:28px;font-weight:700}
.partners{top:814px;left:111px;display:flex;gap:12px}
.partner{width:186px;height:89px;background:var(--white);box-shadow:0 2px 10px rgba(0,0,0,.12);display:flex;align-items:center;justify-content:center;gap:8px;font-family:"Poppins",sans-serif;font-weight:600;font-size:26px;color:#333}
.partner .dot{width:22px;height:22px;border-radius:50%;background:#333}

/* about */
.about-block{top:985px;left:0;width:449px;height:658px;background:var(--charcoal)}
.about-photo{left:152px;top:1053px;width:410px;height:519px;background:linear-gradient(160deg,#d9c6a6,#8f7a55 55%,#4b3f2e)}
.kicker{left:661px;top:1059px;font-family:"Poppins",sans-serif;font-weight:600;font-size:12px;color:var(--red);text-transform:uppercase}
.about-title{left:660px;top:1085px;font-size:38px;color:var(--ink)}
.about-hi{left:662px;top:1143px;font-size:32px;color:var(--ink)}
.about-hi span{color:var(--red)}
.about-text{left:662px;top:1210px;width:420px;font-size:14px;line-height:27.5px;color:var(--grey)}

/* banner */
.banner{top:1733px;left:0;width:1200px;height:183px;background:linear-gradient(100deg,var(--red-dark),var(--red) 40%,#d8141f)}
.banner-title{left:136px;top:38px;font-size:40px;line-height:50px;color:var(--white)}

/* videos */
.section-title{width:1200px;text-align:center;font-size:28px;color:var(--ink)}
.video-main{left:181px;top:2064px;width:837px;height:437px;background:linear-gradient(120deg,#6a5246,#3c2b2a 45%,#2c3a3b 70%,#4c5c56)}
.thumbs{left:181px;top:2513px;display:flex;gap:8.4px}
.thumb{width:97.5px;height:72px;background:linear-gradient(135deg,#8a7062,#3f4544);position:relative}
.thumb .mini-play{position:absolute;left:50%;top:50%;width:20px;height:20px;margin:-10px 0 0 -10px;border-radius:50%;background:rgba(0,0,0,.6);border:1px solid #fff}

/* events */
.events{top:2667px;left:0;width:1200px;height:464px;background:var(--slate)}
.events-red{left:0;top:0;width:390px;height:464px;background:var(--red)}
.events-photo{left:94px;top:68px;width:472px;height:396px;background:radial-gradient(ellipse at 45% 40%,#e0bfa6,#a58b7c 45%,#4a4a4a)}
.events-title{left:633px;top:92px;font-size:34px;color:var(--white)}
.events-meta{left:636px;top:148px;display:flex;gap:34px;font-size:13px;color:var(--white)}
.events-meta span{display:flex;align-items:center;gap:8px}
.events-text{left:636px;top:180px;width:451px;font-size:13px;line-height:24.5px;color:#eee;text-align:justify}
.arrow-btn{width:30px;height:22px;border:1px solid #fff;display:flex;align-items:center;justify-content:center}

/* why */
.cards{left:107px;top:3297px;display:flex;gap:28px}
.card{width:226px;height:195px;border-radius:6px;display:flex;flex-direction:column;align-items:center;justify-content:center;gap:14px;font-family:"Poppins",sans-serif;font-weight:700;font-size:22px;line-height:28px;color:var(--white);text-transform:uppercase;text-align:center}
.card.red{background:var(--red)}
.card.dark{background:var(--charcoal)}

/* feed */
.feed{top:3609px;left:0;width:1200px;height:465px;background:var(--light)}
.feed-red{left:0;top:0;width:474px;height:465px;background:var(--red)}
.feed-title{left:107px;top:102px;font-size:90px;line-height:86px;color:var(--white)}
.feed-follow{left:108px;top:312px;font-size:32px;color:var(--white);display:flex;align-items:center;gap:12px}
.feed-grid{left:546px;top:84px;display:grid;grid-template-columns:repeat(3,174px);grid-template-rows:repeat(2,142px);gap:13px 11px}
.feed-grid div:nth-child(1){background:linear-gradient(135deg,#6b6f56,#c0a78c)}
.feed-grid div:nth-child(2){background:linear-gradient(135deg,#4a5564,#c39b82)}
.feed-grid div:nth-child(3){background:linear-gradient(135deg,#2d5f8c,#b9c7d4)}
.feed-grid div:nth-child(4){background:linear-gradient(180deg,#8fb0d4,#b46d48)}
.feed-grid div:nth-child(5){background:linear-gradient(135deg,#e6e6e6,#2a2a2a)}
.feed-grid div:nth-child(6){background:linear-gradient(135deg,#6d9ad0,#e2cbb8)}

/* contact */
.contact-wave{left:0;top:4429px}
.form-box{left:185px;top:4273px;width:830px;height:355px;background:var(--white);border-top:3px solid var(--red);box-shadow:0 3px 14px rgba(0,0,0,.15)}
.field{position:absolute;height:45px;border:1px solid var(--line);font-size:12px;color:var(--grey);padding:14px 18px}

/* footer */
.foot-head{top:4692px;font-family:"Poppins",sans-serif;font-weight:600;font-size:12px;color:var(--white);text-decoration:underline;text-transform:uppercase}
.foot-list{list-style:none;font-size:13px;color:#ddd}
.foot-list li{height:37px;display:flex;align-items:flex-start;gap:12px}
.foot-list li::before{content:"»";color:#ccc}
.contact-list li{display:flex;gap:14px;font-size:13px;color:#ddd;line-height:25px}
.news{left:795px;top:4740px;width:287px;height:45px;background:var(--white);display:flex}
.news span{flex:1;padding:14px 16px;font-size:13px;color:var(--grey)}
.news b{width:49px;background:var(--red);display:flex;align-items:center;justify-content:center}
.foot-rule{left:119px;top:4942px;width:963px;height:1px;background:#555}
.copyright{top:4972px;width:1200px;text-align:center;font-size:13px;color:#ddd}
</style>
</head>
<body>

<header class="abs site-header">
  <div class="abs brand-name">Corinne Valdaux</div>
  <div class="abs brand-tag">Inspirational speaker and coach</div>
  <nav class="abs nav">
    <span class="active">Home</span><span>Public Speaking</span><span>Media Training</span><span>Coach</span><span>About</span><span>Contact</span>
  </nav>
  <div class="btn btn-red" style="left:965px;top:22px;width:131px;height:44px">Book Now
    <svg width="13" height="13" viewBox="0 0 14 14"><rect x="1" y="2" width="12" height="11" fill="none" stroke="#fff" stroke-width="1.5"/><line x1="1" y1="5" x2="13" y2="5" stroke="#fff" stroke-width="1.5"/></svg>
  </div>
</header>

<section class="abs hero">
  <div class="abs hero-photo" role="img" aria-label="Portrait of Corinne Valdaux smiling, long platinum hair"></div>
  <h1 class="abs heading hero-title">No one can<br>do this alone<br>&amp; <span class="accent">Succeed</span></h1>
  <p class="abs hero-sub">So find those that elevate you rise together better &amp; faster</p>
  <div class="abs hero-sign" role="img" aria-label="Handwritten signature of Corinne Valdaux"></div>
</section>

<h2 class="abs heading trusted-title" style="font-size:28px">Trusted by the world's best</h2>
<div class="abs partners">
  <div class="partner"><i class="dot"></i>Orvane</div>
  <div class="partner"><i class="dot"></i>Lumio</div>
  <div class="partner"><i class="dot"></i>Brisk</div>
  <div class="partner"><i class="dot"></i>Tessa</div>
  <div class="partner" style="font-size:20px">Nordly.co</div>
</div>

<div class="abs about-block"></div>
<div class="abs about-photo" role="img" aria-label="Corinne Valdaux holding a crown toward the camera"></div>
<p class="abs kicker">Build your winning mindset. Build your winning life.</p>
<h2 class="abs heading about-title">I can help you win</h2>
<p class="abs script about-hi">Hi, I'm <span>Corinne Valdaux</span></p>
<p class="abs about-text">Lorem ipsum dolor sit amet, consectetur adipiscing elit, sed do eiusmod tempor incididunt ut labore et dolore magna aliqua. Ut enim ad minim veniam, quis nostrud exercitation ullamco laboris nisi ut aliquip ex ea commodo consequat. Duis aute irure dolor in reprehenderit in voluptate velit esse cillum dolore eu fugiat nulla pariatur. Excepteur sint occaecat cupidatat non proident, sunt in culpa qui officia deserunt mollit anim id est laborum Lorem ipsum dolor sit amet, consectetur adipiscing elit, sed do eiusmod tempor incididunt ut labore et dolore magna aliqua. Ut enim ad minim veniam, quis nostrud exercitation</p>
<div class="btn btn-red" style="left:662px;top:1516px;width:308px;height:52px">Book your first event now
  <svg width="13" height="13" viewBox="0 0 14 14"><rect x="1" y="2" width="12" height="11" fill="none" stroke="#fff" stroke-width="1.5"/><line x1="1" y1="5" x2="13" y2="5" stroke="#fff" stroke-width="1.5"/></svg>
</div>

<section class="abs banner">
  <h2 class="abs heading banner-title">Have Corinne Valdaux speak at<br>your next event</h2>
  <div class="btn btn-dark" style="left:934px;top:72px;width:129px;height:43px">Book Now
    <svg width="13" height="13" viewBox="0 0 14 14"><rect x="1" y="2" width="12" height="11" fill="none" stroke="#fff" stroke-width="1.5"/><line x1="1" y1="5" x2="13" y2="5" stroke="#fff" stroke-width="1.5"/></svg>
  </div>
</section>

<h2 class="abs heading section-title" style="top:1996px">Our Videos</h2>
<div class="abs video-main" role="img" aria-label="Video still: collage of family photos with the caption True change happens">
  <svg class="abs" style="left:397px;top:201px" width="44" height="44" viewBox="0 0 44 44"><circle cx="22" cy="22" r="22" fill="#ee1c2e"/><polygon points="17,13 31,22 17,31" fill="#fff"/></svg>
</div>
<div class="abs thumbs">
  <div class="thumb"></div><div class="thumb"><i class="mini-play"></i></div><div class="thumb"><i class="mini-play"></i></div><div class="thumb"><i class="mini-play"></i></div><div class="thumb"><i class="mini-play"></i></div><div class="thumb"><i class="mini-play"></i></div><div class="thumb"><i class="mini-play"></i></div><div class="thumb"><i class="mini-play"></i></div>
</div>

<section class="abs events">
  <div class="abs events-red"></div>
  <div class="abs events-photo" role="img" aria-label="Close-up portrait of Corinne Valdaux at an event"></div>
  <h2 class="abs heading events-title">Latest Events</h2>
  <div class="abs events-meta">
    <span><svg width="12" height="12" viewBox="0 0 14 14"><rect x="1" y="2" width="12" height="11" fill="#ee1c2e"/></svg>20/08/2021</span>
    <span><svg width="12" height="12" viewBox="0 0 14 14"><circle cx="7" cy="4" r="3" fill="#ee1c2e"/><path d="M1 14a6 6 0 0 1 12 0z" fill="#ee1c2e"/></svg>Corinne Valdaux</span>
  </div>
  <p class="abs events-text">Sed ut perspiciatis unde omnis iste natus error sit voluptatem accusantium doloremque laudantium, totam rem aperiam, eaque ipsa quae ab illo inventore veritatis et quasi architecto beatae vitae dicta sunt explicabo. Nemo enim ipsam voluptatem quia voluptas sit aspernatur aut odit aut fugit, sed quia consequuntur magni dolores eos qui ratione voluptatem sequi nesciunt. Neque porro quisquam est, qui dolorem ipsum quia dolor sit amet, consectetur</p>
  <div class="abs" style="left:636px;top:364px;display:flex;gap:14px">
    <span class="arrow-btn"><svg width="16" height="10" viewBox="0 0 16 10"><path d="M15 5H2M6 1L2 5l4 4" stroke="#fff" stroke-width="2" fill="none"/></svg></span>
    <span class="arrow-btn"><svg width="16" height="10" viewBox="0 0 16 10"><path d="M1 5h13M10 1l4 4-4 4" stroke="#fff" stroke-width="2" fill="none"/></svg></span>
  </div>
</section>

<h2 class="abs heading section-title" style="top:3210px">Why choose us</h2>
<div class="abs cards">
  <div class="card red"><svg width="64" height="56" viewBox="0 0 64 56" fill="none" stroke="#fff" stroke-width="3"><circle cx="32" cy="10" r="7"/><circle cx="14" cy="30" r="5"/><circle cx="32" cy="30" r="5"/><circle cx="50" cy="30" r="5"/><path d="M6 52c0-8 16-8 16 0M24 52c0-8 16-8 16 0M42 52c0-8 16-8 16 0"/></svg><span>Thought<br>Leader</span></div>
  <div class="card dark"><svg width="64" height="56" viewBox="0 0 64 56" fill="#fff"><circle cx="32" cy="10" r="8"/><path d="M20 36c0-12 24-12 24 0z"/><circle cx="12" cy="30" r="6"/><circle cx="52" cy="30" r="6"/><path d="M2 52c0-10 20-10 20 0zM42 52c0-10 20-10 20 0zM22 52c0-10 20-10 20 0z"/></svg><span>Keynote<br>Speaker</span></div>
  <div class="card red"><svg width="64" height="56" viewBox="0 0 64 56" fill="#fff"><circle cx="12" cy="12" r="6"/><circle cx="32" cy="8" r="6"/><circle cx="52" cy="12" r="6"/><rect x="6" y="20" width="12" height="30" rx="4"/><rect x="26" y="16" width="12" height="34" rx="4"/><rect x="46" y="20" width="12" height="30" rx="4"/></svg><span>Best<br>Coach</span></div>
  <div class="card dark"><svg width="56" height="56" viewBox="0 0 56 56" fill="#fff"><circle cx="28" cy="10" r="7"/><circle cx="10" cy="14" r="6"/><circle cx="46" cy="14" r="6"/><rect x="20" y="20" width="16" height="32" rx="5"/><rect x="3" y="22" width="14" height="26" rx="5"/><rect x="39" y="22" width="14" height="26" rx="5"/></svg><span>Consulting</span></div>
</div>

<section class="abs feed">
  <div class="abs feed-red"></div>
  <h2 class="abs heading feed-title">Photo<br>Feed</h2>
  <p class="abs script feed-follow">Give us a follow <svg width="22" height="10" viewBox="0 0 22 10"><path d="M1 5h18M15 1l4 4-4 4" stroke="#fff" stroke-width="2" fill="none"/></svg></p>
  <div class="abs feed-grid">
    <div role="img" aria-label="Child feeding a horse at a fence"></div>
    <div role="img" aria-label="Group of friends smiling together"></div>
    <div role="img" aria-label="Shop shelves stocked with products"></div>
    <div role="img" aria-label="Hiker with arms raised above a canyon"></div>
    <div role="img" aria-label="Black and white photo with a cat"></div>
    <div role="img" aria-label="Selfie of Corinne Valdaux by the water"></div>
  </div>
</section>

<svg class="abs contact-wave" width="1200" height="596" viewBox="0 0 1200 596"><path d="M0 0 L600 120 L1200 0 V596 H0 Z" fill="#2b2b2b"/></svg>
<h2 class="abs heading section-title" style="top:4200px">Get in touch</h2>
<div class="abs form-box">
  <div class="field" style="left:30px;top:55px;width:345px">Enter Your Name</div>
  <div class="field" style="left:30px;top:111px;width:345px">Enter Your Email</div>
  <div class="field" style="left:30px;top:167px;width:345px">Enter Your Phone No</div>
  <div class="field" style="left:30px;top:223px;width:345px">Phone</div>
  <div class="field" style="left:411px;top:57px;width:387px">Any Time</div>
  <div class="field" style="left:411px;top:112px;width:387px;height:94px">Message</div>
  <div class="btn btn-red" style="left:411px;top:227px;width:158px;height:43px">Submit Now
    <svg width="13" height="13" viewBox="0 0 14 14"><circle cx="7" cy="7" r="6" fill="#fff"/><path d="M6 4l3 3-3 3" stroke="#ee1c2e" stroke-width="1.6" fill="none"/></svg>
  </div>
</div>

<footer>
  <div class="abs foot-head" style="left:119px">Optimize</div>
  <ul class="abs contact-list" style="left:119px;top:4724px;list-style:none">
    <li><svg width="12" height="16" viewBox="0 0 12 16" style="margin-top:5px"><path d="M6 0a6 6 0 0 1 6 6c0 4-6 10-6 10S0 10 0 6a6 6 0 0 1 6-6z" fill="#fff"/><circle cx="6" cy="6" r="2" fill="#2b2b2b"/></svg><span>12/48 Harbor Lane<br>United States</span></li>
    <li style="margin-top:10px"><svg width="13" height="13" viewBox="0 0 14 14" style="margin-top:6px"><path d="M3 1l3 3-2 2c1 2 2 3 4 4l2-2 3 3-2 2C6 13 1 8 1 3z" fill="#fff"/></svg><span>1 800 555 0142</span></li>
    <li style="margin-top:10px"><svg width="14" height="11" viewBox="0 0 14 11" style="margin-top:7px"><rect width="14" height="11" fill="#fff"/><path d="M0 0l7 6 7-6" stroke="#2b2b2b" fill="none"/></svg><span>hello@corinnevaldaux.com</span></li>
  </ul>
  <div class="abs foot-head" style="left:402px">Quick Links</div>
  <ul class="abs foot-list" style="left:402px;top:4727px"><li>Home</li><li>About Us</li><li>Our Videos</li><li>Resources</li><li>Testimonials</li></ul>
  <div class="abs foot-head" style="left:586px">Other Links</div>
  <ul class="abs foot-list" style="left:586px;top:4727px"><li>Terms &amp; Conditions</li><li>Privacy Policy</li><li>Help Service</li><li>FAQ</li><li>Contact us</li></ul>
  <div class="abs foot-head" style="left:795px;top:4690px">Subscribe to our newsletter</div>
  <div class="abs news"><span>Email Address</span><b><svg width="18" height="18" viewBox="0 0 18 18"><path d="M17 1L1 8l7 2 2 7z" fill="#fff"/></svg></b></div>
  <div class="abs foot-rule"></div>
  <p class="abs copyright">© 2021 Corinne Valdaux. All Rights Reserved</p>
</footer>

</body>
</html>
```